Brookside Grocer

Hope all is well!

Wanted to make business cards for my father. His name is Faisal Qureshi and owns convenience stores. I have attached logo :)

He does not want any title just simple name and phone. An email would be nice as well.

Faisal Qureshi
Cell: 413-585-2046
Store: 413-719-4820

Brooksidegrocer512@fernpost.com

The design and style is totally up to you :) The colors we were looking for were the same as logo :)

```html
<!DOCTYPE html>
<html lang="en">
<head>
<meta charset="utf-8">
<title>Brookside Grocer – Business Cards</title>
<link href="https://fonts.googleapis.com/css2?family=Montserrat:wght@400;500;600;700&display=swap" rel="stylesheet">
<style>
  :root {
    --backdrop: #e9e6e1;
    --card: #fbfbfd;
    --navy: #243a7a;
    --red: #e8323a;
    --ink: #1e1e1e;
  }
  * { margin: 0; padding: 0; box-sizing: border-box; }
  html, body { width: 900px; height: 1200px; overflow: hidden; }
  body {
    position: relative;
    background: var(--backdrop);
    font-family: "Montserrat", Arial, sans-serif;
    color: var(--ink);
  }
  .card {
    position: absolute;
    left: 68px;
    width: 758px;
    background: var(--card);
    border-radius: 30px;
  }
  .card--front { top: 133px; height: 440px; }
  .card--back  { top: 637px; height: 450px; }

  .brand-name {
    position: absolute;
    color: var(--navy);
    font-weight: 700;
    white-space: nowrap;
    letter-spacing: 0.5px;
  }
  .card--front .brand-name {
    left: 217px; top: 242px;
    transform: translate(-50%, -50%);
    font-size: 34px;
  }
  .card--back .brand-name {
    left: 50%; top: 50%;
    transform: translate(-50%, -50%);
    font-size: 64px;
  }

  .divider {
    position: absolute;
    left: 416px; top: 135px;
    width: 2px; height: 208px;
    background: var(--red);
  }
  .contact {
    position: absolute;
    left: 444px; top: 135px;
    height: 208px;
    display: flex;
    flex-direction: column;
    justify-content: center;
  }
  .contact__name {
    color: var(--red);
    font-weight: 700;
    font-size: 26px;
    line-height: 30px;
    margin-bottom: 16px;
  }
  .contact__list { list-style: none; }
  .contact__item {
    display: flex;
    align-items: center;
    font-size: 15px;
    line-height: 23px;
    height: 24px;
    white-space: nowrap;
  }
  .contact__icon {
    width: 14px; height: 14px;
    margin: 0 12px 0 6px;
    fill: var(--red);
    flex: none;
  }
</style>
</head>
<body>
  <section class="card card--front">
    <div class="brand-name">Brookside Grocer</div>
    <div class="divider"></div>
    <div class="contact">
      <div class="contact__name">Faisal Qureshi</div>
      <ul class="contact__list">
        <li class="contact__item">
          <svg class="contact__icon" viewBox="0 0 16 16" aria-hidden="true"><path d="M1 6c0-2 3-4 7-4s7 2 7 4v1h-3.5V5.5h-7V7H1z"/><path d="M4 8h8l2 6H2z"/></svg>
          413-719-4820
        </li>
        <li class="contact__item">
          <svg class="contact__icon" viewBox="0 0 16 16" aria-hidden="true"><path d="M4.5 0h7A1.5 1.5 0 0 1 13 1.5v13a1.5 1.5 0 0 1-1.5 1.5h-7A1.5 1.5 0 0 1 3 14.5v-13A1.5 1.5 0 0 1 4.5 0zM5 2v10h6V2zm3 11a1 1 0 1 0 0 2 1 1 0 0 0 0-2z"/></svg>
          413-585-2046
        </li>
        <li class="contact__item">
          <svg class="contact__icon" viewBox="0 0 16 16" aria-hidden="true"><path d="M1 4h14v1L8 9.5 1 5z"/><path d="M1 6.5l7 4.5 7-4.5V13H1z"/></svg>
          Brooksidegrocer512@fernpost.com
        </li>
      </ul>
    </div>
  </section>

  <section class="card card--back">
    <div class="brand-name">Brookside Grocer</div>
  </section>
</body>
</html>
```